Logo is done, need templates now

I want to be able to have an email template, same for word documents, powerpoint etc. I have the logo, now I need all the pieces for appearance in correspondence and marketing

Target Market(s)

Professional Advisors and Wealthy Clients

Font styles to use
Serif

Requirements
Must have
• I want to be able to do word documents and email them with letterhead. I need great email signatures. I need similar formatting for the word documents to be flexible to add to powerpoint and other presentations.

```html
<!DOCTYPE html>
<html lang="en">
<head>
<meta charset="UTF-8">
<title>Stillwell Capital Letterhead</title>
<link rel="stylesheet" href="https://fonts.googleapis.com/css2?family=IBM+Plex+Sans:wght@400;500;700&display=swap">
<style>
  :root {
    --brand-blue: #0a0898;
    --charcoal: #444444;
    --ink: #000000;
    --paper: #ffffff;
  }
  * { margin: 0; padding: 0; box-sizing: border-box; }
  html, body {
    width: 927px;
    height: 1200px;
    overflow: hidden;
    background: var(--paper);
  }
  .letterhead {
    position: relative;
    width: 927px;
    height: 1200px;
    background: var(--paper);
    font-family: "IBM Plex Sans", sans-serif;
    overflow: hidden;
  }
  .frame-shapes {
    position: absolute;
    inset: 0;
  }
  .company-name {
    position: absolute;
    top: 118px;
    left: 0;
    width: 927px;
    text-align: center;
    font-size: 26px;
    font-weight: 400;
    letter-spacing: 0.32em;
    color: var(--charcoal);
    padding-left: 0.32em;
    white-space: nowrap;
  }
  .signer-name {
    position: absolute;
    left: 53px;
    top: 919px;
    font-size: 33px;
    font-weight: 700;
    letter-spacing: 0.02em;
    color: var(--paper);
    line-height: 1;
    white-space: nowrap;
  }
  .signer-title {
    position: absolute;
    left: 93px;
    top: 993px;
    font-size: 33px;
    font-weight: 500;
    color: var(--ink);
    line-height: 1;
  }
  .contact-list {
    position: absolute;
    left: 56px;
    top: 1053px;
    list-style: none;
  }
  .contact-item {
    display: flex;
    align-items: center;
    height: 35.5px;
    font-size: 22px;
    color: var(--brand-blue);
    white-space: nowrap;
  }
  .contact-icon {
    width: 21px;
    height: 21px;
    margin-right: 8px;
    flex: none;
    fill: var(--brand-blue);
  }
</style>
</head>
<body>
<main class="letterhead">
  <svg class="frame-shapes" width="927" height="1200" viewBox="0 0 927 1200" aria-hidden="true">
    <polygon class="header-band-left" points="0,50 282,50 249,125 0,125" fill="var(--brand-blue)"/>
    <polygon class="header-band-right" points="645,50 927,50 927,125 679,125" fill="var(--brand-blue)"/>
    <rect class="side-rule" x="33" y="125" width="9" height="1075" fill="var(--charcoal)"/>
    <polyline class="name-band-outline" points="300,911 322,911 286,985 0,985" fill="none" stroke="var(--charcoal)" stroke-width="2.5"/>
    <polygon class="name-band" points="0,904 304,904 271,979 0,979" fill="var(--brand-blue)"/>
  </svg>

  <div class="company-name">STILLWELL CAPITAL</div>

  <div class="signer-name">ADAM PRICE</div>
  <div class="signer-title">Director</div>

  <ul class="contact-list">
    <li class="contact-item">
      <svg class="contact-icon" viewBox="0 0 24 24" aria-hidden="true">
        <rect x="1" y="1" width="22" height="22" rx="4"/>
        <path d="M8.2 5.5l2 3-1.3 1.4c.8 1.8 2.3 3.3 4.2 4.2l1.4-1.3 3 2-.9 2.6c-5.8.2-11-5-10.9-10.9z" fill="#fff"/>
      </svg>
      415,555,0142
    </li>
    <li class="contact-item">
      <svg class="contact-icon" viewBox="0 0 24 24" aria-hidden="true">
        <rect x="1" y="4" width="22" height="16" rx="2"/>
        <path d="M3.5 7l8.5 6 8.5-6" fill="none" stroke="#fff" stroke-width="2"/>
      </svg>
      hello@example.com
    </li>
    <li class="contact-item">
      <svg class="contact-icon" viewBox="0 0 24 24" aria-hidden="true">
        <path d="M12 0C7 0 3.5 3.6 3.5 8.3 3.5 14 12 24 12 24s8.5-10 8.5-15.7C20.5 3.6 17 0 12 0z"/>
        <circle cx="12" cy="8.5" r="3.3" fill="#fff"/>
      </svg>
      Elm Street, Harbor Square.
    </li>
    <li class="contact-item">
      <svg class="contact-icon" viewBox="0 0 24 24" aria-hidden="true">
        <circle cx="12" cy="12" r="11.5"/>
        <text x="12" y="13.5" font-size="6" font-family="IBM Plex Sans, sans-serif" fill="#fff" text-anchor="middle">www</text>
        <path d="M14 15l4 4M14 15v3M14 15h3" stroke="#fff" stroke-width="1" fill="none"/>
      </svg>
      www.example.com
    </li>
  </ul>
</main>
</body>
</html>
```